ultra-minimalist business card

front (black background, matte):

tarik b. hosseny
writer | photographer
get@tarikhosseny.com

back (white background, matte):

a picture speaks a thousand words;
a word draws a thousand pictures.

www.tarikhosseny.com

all text should be small (white or silver - as long as it shows against the black - on the front; black or gray - as long as it shows against the white - on the back).

feel free to get creative in terms of arrangement, alignment, and font type, but remember, the overall style is minimalist, so nothing too fancy, please.

thanks.

```html
<!DOCTYPE html>
<html lang="en">
<head>
<meta charset="utf-8">
<title>Tarik B. Hosseny — Business Card</title>
<link rel="stylesheet" href="https://fonts.googleapis.com/css2?family=Libre+Baskerville:wght@400;700&display=swap">
<style>
  :root {
    --stage: #1c1c1c;
    --card-black: #0b0b0b;
    --card-white: #f4f3f0;
    --silver: #e6e6e6;
    --silver-soft: #a9a9a9;
    --ink: #3a3a3a;
    --ink-soft: #555555;
  }

  * { margin: 0; padding: 0; box-sizing: border-box; }

  html, body {
    width: 1200px;
    height: 852px;
    overflow: hidden;
  }

  body {
    background: var(--stage);
    display: flex;
    align-items: center;
    justify-content: center;
    gap: 60px;
    font-family: "Libre Baskerville", Georgia, serif;
  }

  .card {
    position: relative;
    width: 510px;
    height: 292px;
    box-shadow: 0 14px 30px rgba(0, 0, 0, 0.45);
  }

  /* Front */
  .card--front {
    background: var(--card-black);
    color: var(--silver);
    text-align: center;
  }

  .card__name {
    position: absolute;
    top: 112px;
    left: 0;
    right: 0;
    font-size: 15px;
    font-weight: 700;
    letter-spacing: 0.06em;
    text-transform: uppercase;
  }

  .card__role {
    position: absolute;
    top: 137px;
    left: 0;
    right: 0;
    font-size: 9px;
    color: var(--silver-soft);
    letter-spacing: 0.04em;
  }

  .card__email {
    position: absolute;
    bottom: 40px;
    left: 0;
    right: 0;
    font-size: 8.5px;
    color: var(--silver-soft);
    letter-spacing: 0.03em;
  }

  /* Back */
  .card--back {
    background: var(--card-white);
    color: var(--ink);
  }

  .card__quote {
    position: absolute;
    top: 140px;
    left: 0;
    right: 0;
    text-align: center;
    font-size: 11.5px;
    line-height: 1.75;
    letter-spacing: 0.22em;
  }

  .card__web {
    position: absolute;
    top: 218px;
    right: 88px;
    font-size: 9px;
    color: var(--ink-soft);
    letter-spacing: 0.03em;
  }
</style>
</head>
<body>
  <section class="card card--front" aria-label="Card front">
    <h1 class="card__name">Tarik B. Hosseny</h1>
    <p class="card__role">Writer | Photographer</p>
    <p class="card__email">get@tarikhosseny.com</p>
  </section>

  <section class="card card--back" aria-label="Card back">
    <p class="card__quote">A picture speaks a thousand words<br>A word draws a thousand pictures</p>
    <p class="card__web">www.tarikhosseny.com</p>
  </section>
</body>
</html>
```